Business Postcard Design for Personal Training Company

Need a postcard design for my company called "Cobalt Stride" Colors are Navy Blue, Blue, Grey and White.

On the front I want there to be pictures and it to feature a box that says "Free Consultation + 50% off your first session!"

And somehow to feature the following phrases " Lose Weight. Gain Muscle."
"Customized Personal training using V-Core, the latest technology in fitness. Reach your fitness goals in just two 25-min sessions per week"

Also want featured the following phrases (maybe on back):

"up to 18 times more effective than a conventional gym workout"

I need the back of the postcard to have all my business information:

Address: 327 Venadero Ave, Building B Suite 518, Costa Mesa CA 92626
Website: cobalt-stride.example
Phone #: (949) 555-0137
E-mail: cobaltstridehealth@mailbox.example

I am going to upload my logo, before and after pictures and pictures of people training on the device. Feel free to use as many/or little photos as you want.

Target Market(s)

Wealthy Adults 40+ years old looking for a personal trainer

Industry/Entity Type

Personal Trainer

Colors
0455a3
85cae6
aaaaaa
ffffff

Requirements
Must have
• At least two of the before and after photos, and two or more photos of people working out on the device.

```html
<!DOCTYPE html>
<html lang="en">
<head>
<meta charset="utf-8">
<title>Cobalt Stride Postcard</title>
<link rel="stylesheet" href="https://fonts.googleapis.com/css2?family=Oswald:wght@400;500;600&family=Ubuntu:wght@400;500;700&display=swap">
<style>
  :root{
    --navy:#0455a3;
    --blue:#1e9bd7;
    --sky:#85cae6;
    --grey:#aaaaaa;
    --slate:#56524c;
    --ink:#222222;
    --white:#ffffff;
    --paper-grey:#ebebeb;
    --backdrop:#9c9c9c;
  }
  *{box-sizing:border-box;margin:0;padding:0}
  html,body{width:1200px;height:1200px;overflow:hidden}
  body{background:var(--backdrop);position:relative;font-family:"Ubuntu",sans-serif}

  .postcard{position:absolute;overflow:hidden;background:var(--white)}
  .postcard--front{left:226px;top:18px;width:741px;height:570px}
  .postcard--back{left:226px;top:612px;width:740px;height:564px;background:var(--paper-grey)}

  /* front */
  .photo-layer{position:absolute;inset:0}
  .brand{position:absolute;display:flex;align-items:center;gap:10px;color:#8a8a8a;font-family:"Ubuntu",sans-serif;font-weight:700;letter-spacing:1px}
  .brand__dot{border-radius:50%;background:var(--sky)}
  .postcard--front .brand{left:58px;top:88px;font-size:30px}
  .postcard--front .brand__dot{width:22px;height:22px}

  .tagline{position:absolute;left:14px;top:202px;font-family:"Oswald",sans-serif;font-weight:600;font-size:24px;color:var(--blue);letter-spacing:.5px}

  .offer{position:absolute;left:0;top:252px;width:350px;height:90px;background:var(--blue);color:var(--white);text-align:center;font-family:"Oswald",sans-serif;padding-top:8px}
  .offer__title{font-size:35px;font-weight:500;line-height:1.05;padding-right:20px}
  .offer__sub{font-size:22px;font-weight:400;padding-right:20px}

  .pitch{position:absolute;left:0;top:360px;width:330px;height:96px;background:var(--slate);color:var(--white);font-family:"Oswald",sans-serif;font-weight:500;font-size:13.5px;line-height:18.5px;padding:11px 30px 0 16px;text-transform:uppercase}

  .front-address{position:absolute;left:16px;top:480px;display:flex;gap:10px;color:var(--ink);font-size:19px;line-height:25px}
  .front-address svg{flex:none;margin-top:4px}

  .web-band{position:absolute;left:456px;top:528px;width:285px;height:42px;background:rgba(20,50,80,.55);color:var(--white);font-size:19px;display:flex;align-items:center;justify-content:flex-end;padding-right:16px}

  /* back */
  .back-photo{position:absolute;left:0;top:0;width:359px;height:180px;background:linear-gradient(180deg,#c9d6de 0%,#9fb0b4 38%,#5f7a48 70%,#4a6a36 100%)}
  .back-logo{position:absolute;left:359px;top:0;width:207px;height:180px;background:var(--white)}
  .postcard--back .brand{left:16px;top:74px;font-size:19px;gap:7px}
  .postcard--back .brand__dot{width:14px;height:14px}
  .postage{position:absolute;left:566px;top:10px;width:162px;height:170px;color:#9a9a9a;font-size:19px;text-align:center;padding-top:62px;line-height:24px}
  .area-label{position:absolute;color:#a3a3a3;font-size:19px}

  .back-panel{position:absolute;left:0;top:180px;width:359px;height:288px;background:var(--white)}
  .claim{position:absolute;left:0;top:8px;width:359px;height:66px;background:var(--blue);color:var(--white);font-family:"Oswald",sans-serif;font-weight:500;font-size:20px;line-height:27px;padding:7px 0 0 20px;text-transform:uppercase}
  .contact-tab{position:absolute;left:0;top:84px;width:140px;height:30px;background:var(--blue);color:var(--white);font-family:"Oswald",sans-serif;font-weight:500;font-size:20px;line-height:30px;padding-left:20px;clip-path:polygon(0 0,100% 0,92% 100%,0 100%)}
  .contact-list{position:absolute;left:18px;top:128px;list-style:none;color:var(--ink);font-size:18px}
  .contact-list li{display:flex;align-items:flex-start;gap:14px;line-height:23px;margin-bottom:10px}
  .contact-list svg{flex:none;margin-top:5px}
  .contact-list .phone{font-weight:700}
</style>
</head>
<body>

<section class="postcard postcard--front" aria-label="Postcard front">
  <svg class="photo-layer" width="741" height="570" viewBox="0 0 741 570">
    <defs>
      <linearGradient id="studioTone" x1="0" y1="0" x2="1" y2="1">
        <stop offset="0" stop-color="#e6e9ec"/>
        <stop offset=".55" stop-color="#b7bcc3"/>
        <stop offset="1" stop-color="#3d4a6a"/>
      </linearGradient>
      <linearGradient id="portraitTone" x1="0" y1="0" x2="0" y2="1">
        <stop offset="0" stop-color="#ece9e4"/>
        <stop offset="1" stop-color="#4a4a4f"/>
      </linearGradient>
    </defs>
    <circle cx="830" cy="420" r="516" fill="none" stroke="#e4f3fa" stroke-width="10"/>
    <circle cx="830" cy="420" r="508" fill="none" stroke="var(--blue)" stroke-width="14"/>
    <circle cx="830" cy="420" r="500" fill="url(#studioTone)" role="img" aria-label="Photo of a trainer guiding a client working out on a stability ball with the V-Core suit and control unit"/>
    <circle cx="494" cy="96" r="72" fill="var(--white)"/>
    <circle cx="494" cy="96" r="67" fill="url(#portraitTone)" role="img" aria-label="Before and after photos of a client"/>
    <circle cx="364" cy="288" r="62" fill="var(--white)"/>
    <circle cx="364" cy="288" r="57" fill="url(#portraitTone)" role="img" aria-label="Before and after side-view photos of a client"/>
    <circle cx="338" cy="486" r="62" fill="var(--white)"/>
    <circle cx="338" cy="486" r="57" fill="url(#studioTone)" role="img" aria-label="Photo of a client doing a plank in the training suit"/>
  </svg>

  <div class="brand"><span class="brand__dot"></span>COBALT STRIDE</div>
  <p class="tagline">LOSE WEIGHT. GAIN MUSCLE.</p>

  <div class="offer">
    <p class="offer__title">FREE CONSULTATION</p>
    <p class="offer__sub">+ 50% off your first session!</p>
  </div>

  <p class="pitch">Customized personal training using V-Core, the latest technology in fitness. Reach your fitness goals in just two 25-min sessions per week</p>

  <div class="front-address">
    <svg width="16" height="22" viewBox="0 0 16 22"><path d="M8 0a8 8 0 0 0-8 8c0 6 8 14 8 14s8-8 8-14a8 8 0 0 0-8-8zm0 11a3 3 0 1 1 0-6 3 3 0 0 1 0 6z" fill="var(--blue)"/></svg>
    <p>327 Venadero Ave,<br>Building B Suite 518,<br>Costa Mesa CA 92626</p>
  </div>

  <div class="web-band">www.cobalt-stride.example</div>
</section>

<section class="postcard postcard--back" aria-label="Postcard back">
  <div class="back-photo" role="img" aria-label="Photo of two women training with the V-Core device on a lawn overlooking a harbor"></div>
  <div class="back-logo"><div class="brand"><span class="brand__dot"></span>COBALT STRIDE</div></div>
  <div class="postage">Postage<br>Area</div>
  <p class="area-label" style="left:432px;top:224px">Address Area</p>

  <div class="back-panel">
    <p class="claim">Up to 18 times more effective than<br>a conventional gym workout</p>
    <p class="contact-tab">CONTACT US</p>
    <ul class="contact-list">
      <li>
        <svg width="12" height="16" viewBox="0 0 16 22"><path d="M8 0a8 8 0 0 0-8 8c0 6 8 14 8 14s8-8 8-14a8 8 0 0 0-8-8zm0 11a3 3 0 1 1 0-6 3 3 0 0 1 0 6z" fill="var(--blue)"/></svg>
        <span>327 Venadero Ave, Building B<br>Suite 518, Costa Mesa CA 92626</span>
      </li>
      <li>
        <svg width="14" height="12" viewBox="0 0 14 12"><path d="M1 4c0-2 3-3 6-3s6 1 6 3v1h-3V4H4v1H1zM3 6h8l2 5H1z" fill="var(--blue)"/></svg>
        <span class="phone">(949) 555-0137</span>
      </li>
      <li>
        <svg width="14" height="11" viewBox="0 0 14 11"><rect width="14" height="11" rx="1" fill="var(--blue)"/><path d="M1 1l6 5 6-5" stroke="#fff" stroke-width="1.4" fill="none"/></svg>
        <span>cobaltstridehealth@mailbox.example</span>
      </li>
      <li>
        <svg width="14" height="14" viewBox="0 0 14 14"><circle cx="7" cy="7" r="6" fill="none" stroke="var(--blue)" stroke-width="1.5"/><ellipse cx="7" cy="7" rx="2.6" ry="6" fill="none" stroke="var(--blue)" stroke-width="1.2"/><path d="M1 7h12" stroke="var(--blue)" stroke-width="1.2"/></svg>
        <span>cobalt-stride.example</span>
      </li>
    </ul>
  </div>

  <p class="area-label" style="left:342px;top:506px">Barcode Area</p>
</section>

</body>
</html>
```